Bookcover: Lessons From the Silent Orchard

I am publishing a super-low-cost innovation book for €4,99 on Bravolo Self Release to help everyone become a great innovator: young ambitious people without college education nor a big budget. Do you want to help me?

Brief:
Design a book cover 1600 x 2560 pixels for BSR.
Main title: Lessons From the Silent Orchard
Sub title: mindset - insights - skills & tools
Author: Maarten de Klerk
Design: captive, and appealing to everyone
Target Group: young ambitious people without college education

For bravolo please format the height/width ratio of 1.6:1

```html
<!DOCTYPE html>
<html lang="en">
<head>
<meta charset="utf-8">
<title>Lessons From the Silent Orchard — Book Cover</title>
<link href="https://fonts.googleapis.com/css2?family=Lato:wght@400;700;900&display=swap" rel="stylesheet">
<style>
  :root {
    --backdrop: #dae6f1;
    --orange: #ff8c00;
    --butter: #fddf7a;
    --navy: #003d7c;
    --white: #ffffff;
    --glow: #e9ec8a;
  }
  * { margin: 0; padding: 0; box-sizing: border-box; }
  html, body {
    width: 1200px;
    height: 1200px;
    overflow: hidden;
    background: var(--backdrop);
    font-family: "Lato", sans-serif;
  }
  .cover {
    position: absolute;
    left: 322px;
    top: 155px;
    width: 556px;
    height: 890px;
    overflow: hidden;
  }
  .band { position: absolute; left: 0; width: 100%; }
  .band--top { top: 0; height: 427px; background: var(--orange); }
  .band--middle { top: 427px; height: 290px; background: var(--butter); }
  .band--bottom { top: 717px; height: 173px; background: var(--navy); }

  .title {
    position: absolute;
    left: 41px;
    top: 60px;
    color: var(--white);
  }
  .title__lead {
    display: block;
    font-weight: 700;
    font-size: 29px;
    letter-spacing: 7px;
    line-height: 1;
  }
  .title__main {
    display: block;
    margin-top: 16px;
    font-weight: 900;
    font-size: 86px;
    line-height: 70px;
    letter-spacing: -1px;
  }

  .portrait {
    position: absolute;
    left: 66px;
    top: 291px;
    width: 407px;
    height: 426px;
    border-radius: 46% 46% 0 0 / 30% 30% 0 0;
    background: radial-gradient(circle at 52% 40%, var(--glow) 0 14%, #8fb06a 20%, var(--navy) 34%);
  }

  .subtitle {
    position: absolute;
    top: 748px;
    left: 0;
    width: 100%;
    text-align: center;
    color: var(--butter);
    font-weight: 400;
    font-size: 18px;
    letter-spacing: 4px;
  }
  .author {
    position: absolute;
    top: 800px;
    left: 0;
    width: 100%;
    text-align: center;
    color: var(--white);
    font-weight: 700;
    font-size: 34px;
    letter-spacing: 2px;
  }
</style>
</head>
<body>
  <div class="cover">
    <div class="band band--top"></div>
    <div class="band band--middle"></div>
    <div class="band band--bottom"></div>

    <h1 class="title">
      <span class="title__lead">LESSONS FROM THE</span>
      <span class="title__main">SILENT<br>ORCHARD</span>
    </h1>

    <div class="portrait" role="img" aria-label="Illustration: navy head silhouette in profile with a glowing light bulb inside"></div>

    <p class="subtitle">MINDSET - INSIGHTS - SKILLS &amp; TOOLS</p>
    <p class="author">Maarten de Klerk</p>
  </div>
</body>
</html>
```